Corvello Business card

I got my logo so I need to have that on my business card!!

Thanks
Updates

Reason: Hi designers, i will be deciding my logo by this weekend!!! As soon as I decide i will post my logo for your application Thanks Teodoro

I Just sent my logo for your attention!!!

Target Market(s)

My costumers will be enginners from shipyard industry!

Industry/Entity Type

Business

Requirements
Must have
• My future logo

```html
<!DOCTYPE html>
<html lang="en">
<head>
<meta charset="utf-8">
<title>Corvello Business Card</title>
<link rel="stylesheet" href="https://fonts.googleapis.com/css2?family=Questrial&display=swap">
<style>
  :root {
    --backdrop: #f3eec3;
    --card-front-top: #e0e0e2;
    --card-back: #efefef;
    --logo-disc: #d3d1d2;
    --ink-dark: #6d6e70;
    --ink-mid: #8a8a8c;
    --ink-black: #231f20;
    --green-light: #a8d59a;
    --green-deep: #16967b;
    --green-soft: #5db0a2;
    --white: #ffffff;
  }
  * { box-sizing: border-box; margin: 0; padding: 0; }
  html, body { width: 1200px; height: 1000px; overflow: hidden; }
  body {
    background: var(--backdrop);
    font-family: "Questrial", "Century Gothic", sans-serif;
    position: relative;
  }
  .card { position: absolute; left: 180px; width: 630px; height: 360px; overflow: hidden; }

  /* Front */
  .card--front { top: 99px; background: var(--card-front-top); }
  .logo-disc {
    position: absolute; left: 54px; top: 69px; width: 144px; height: 144px;
    border-radius: 50%; background: var(--logo-disc);
    display: flex; align-items: center; justify-content: center;
    font-size: 15px; color: var(--ink-black);
  }
  .identity { position: absolute; left: 239px; top: 108px; color: var(--ink-dark); }
  .identity__name { font-size: 42px; letter-spacing: -0.5px; line-height: 1; font-weight: 400; }
  .identity__title { font-size: 13px; margin-top: 12px; letter-spacing: -0.2px; }
  .contact-bar { position: absolute; left: 0; top: 251px; width: 630px; height: 109px; display: flex; }
  .contact-bar__item {
    height: 100%; display: flex; flex-direction: column; align-items: center;
    color: var(--white); font-size: 15px; padding-top: 12px;
  }
  .contact-bar__item svg { height: 52px; width: 60px; margin-bottom: 14px; }
  .contact-bar__item--address { width: 206px; background: var(--green-light); }
  .contact-bar__item--phone { width: 219px; background: var(--green-deep); }
  .contact-bar__item--email { width: 205px; background: var(--green-soft); }

  /* Back */
  .card--back { top: 516px; height: 359px; background: var(--card-back); }
  .stripe { position: absolute; }
  .stripe--light { background: var(--green-light); }
  .stripe--deep { background: var(--green-deep); }
  .stripe--soft { background: var(--green-soft); }
  .side-tab { left: 0; width: 74px; }
  .future-logo {
    position: absolute; left: 108px; top: 158px; color: var(--ink-mid);
    font-size: 35px; line-height: 48px; letter-spacing: 1.5px;
  }
  .detail-band {
    left: 353px; width: 277px; color: var(--white); font-size: 15px;
    padding-left: 24px; display: flex; align-items: center;
  }
</style>
</head>
<body>
  <section class="card card--front">
    <div class="logo-disc">LOGO</div>
    <div class="identity">
      <h1 class="identity__name">YOUR NAME</h1>
      <p class="identity__title">YOUR TITLE</p>
    </div>
    <div class="contact-bar">
      <div class="contact-bar__item contact-bar__item--address">
        <svg viewBox="0 0 60 52" aria-hidden="true">
          <path d="M30 3 L3 27 H10 V50 H25 V36 H35 V50 H50 V27 H57 L46 17 V6 H40 V12 Z" fill="#fff"/>
        </svg>
        <span>text here</span>
      </div>
      <div class="contact-bar__item contact-bar__item--phone">
        <svg viewBox="0 0 60 52" aria-hidden="true">
          <circle cx="30" cy="26" r="23" fill="none" stroke="#fff" stroke-width="3"/>
          <path d="M24 13 c-4 2 -6 6 -4 12 c2 7 6 12 12 15 c3 1 6 0 8 -2 l-5 -6 c-1 1 -3 2 -4 1 c-3 -2 -5 -6 -6 -9 c0 -1 1 -2 3 -3 z" fill="#fff"/>
        </svg>
        <span>no phone here</span>
      </div>
      <div class="contact-bar__item contact-bar__item--email">
        <svg viewBox="0 0 60 52" aria-hidden="true">
          <rect x="6" y="10" width="48" height="32" fill="none" stroke="#fff" stroke-width="2"/>
          <path d="M6 10 L30 29 L54 10 M6 42 L24 25 M54 42 L36 25" fill="none" stroke="#fff" stroke-width="2"/>
          <circle cx="30" cy="27" r="5" fill="#fff"/>
        </svg>
        <span>email here</span>
      </div>
    </div>
  </section>

  <section class="card card--back">
    <div class="stripe stripe--light side-tab" style="top:133px;height:42px"></div>
    <div class="stripe stripe--deep side-tab" style="top:175px;height:45px"></div>
    <div class="stripe stripe--soft side-tab" style="top:220px;height:44px"></div>
    <p class="future-logo">Your Future<br>Logo</p>
    <div class="stripe stripe--light detail-band" style="top:133px;height:42px">social network</div>
    <div class="stripe stripe--deep detail-band" style="top:175px;height:45px">website</div>
    <div class="stripe stripe--soft detail-band" style="top:220px;height:44px">fax no</div>
  </section>
</body>
</html>
```